Health Information/Education Logo Design

We need a logo design for a new company based in Atlanta called Meadowlark Health. The program is about patient empowerment. We provide health information and education on how to get healthy, stay healthy, and how to be proactive in your care. We also provide medication and injection training to help patients feel their best and to ensure successful therapy outcomes.
We like the colors yellow, pink, teal and purple and would like to see some or all of these colors in the designs. The final design should communicate caring, considerate, compassionate information, education and training services
Industry/Entity Type
Education
Contact Information for Business Card
Meadowlark Health
Danielle Ostrander RN, MSN, MHA
Nurse Educator
555.214.3096 cell
555.470.2283 fax

```html
<!DOCTYPE html>
<html lang="en">
<head>
<meta charset="utf-8">
<title>Meadowlark Health – Business Card</title>
<link rel="stylesheet" href="https://fonts.googleapis.com/css2?family=Cinzel:wght@400;500;600&family=Tinos:wght@400&display=swap">
<style>
  :root {
    --backdrop: #e7e4df;
    --ink: #161616;
    --black: #050505;
    --white: #ffffff;
    --steel-dark: #1d1d1d;
    --steel-mid: #6b6d6e;
    --steel-light: #d9dbdc;
    --steel-edge: #b9bcbe;
  }
  * { box-sizing: border-box; margin: 0; padding: 0; }
  html, body { width: 1200px; height: 1000px; overflow: hidden; }
  body { background: var(--backdrop); position: relative; }

  .card {
    position: absolute;
    left: 250px;
    width: 700px;
    height: 410px;
    overflow: hidden;
    box-shadow: 0 2px 6px rgba(0,0,0,0.25);
  }

  /* Front */
  .card--front {
    top: 75px;
    background: linear-gradient(to bottom,
      var(--steel-dark) 0%,
      #3a3b3c 30%,
      var(--steel-mid) 44%,
      #b4b6b7 56%,
      var(--steel-light) 66%,
      #cfd1d2 70.5%);
  }
  .card--front .base-strip {
    position: absolute; left: 0; right: 0; top: 290px; bottom: 0;
    background: linear-gradient(to bottom, var(--steel-edge) 0px, #8a8c8d 4px, #2a2a2a 14px, var(--black) 34px);
  }
  .accent-bar { position: absolute; top: 0; background: var(--black); }
  .accent-bar--one { left: 33px; width: 15px; height: 290px; }
  .accent-bar--two { left: 51px; width: 21px; height: 175px; }
  .accent-bar--three { left: 96px; width: 15px; height: 290px; }

  .brand-name {
    position: absolute; left: 0; right: 0;
    font-family: 'Cinzel', serif;
    font-weight: 500;
    text-align: center;
    letter-spacing: 1px;
  }
  .card--front .brand-name { top: 170px; font-size: 40px; color: var(--ink); padding-left: 4px; }

  .holder { position: absolute; left: 28px; top: 328px; color: var(--white); font-family: 'Cinzel', serif; }
  .holder__name { font-size: 28px; font-weight: 500; letter-spacing: 0.5px; }
  .holder__role { font-size: 16.5px; margin-top: 4px; letter-spacing: 0.3px; }

  .contact {
    position: absolute; right: 24px; top: 310px;
    list-style: none; text-align: right;
    font-family: 'Tinos', 'Times New Roman', serif;
    color: var(--white);
  }
  .contact__item { display: flex; justify-content: flex-end; align-items: center; gap: 7px; line-height: 24px; }
  .contact__item--phone { font-size: 21px; letter-spacing: 0.5px; }
  .contact__item--email { font-size: 15.5px; margin-top: 2px; }
  .contact__icon { width: 12px; height: 14px; flex: none; }

  /* Back */
  .card--back {
    top: 513px;
    background: radial-gradient(ellipse at 50% 45%, #111 0%, var(--black) 70%);
  }
  .card--back .brand-name { top: 222px; font-size: 42px; color: var(--white); padding-left: 4px; }
</style>
</head>
<body>

<section class="card card--front" aria-label="Business card front">
  <div class="accent-bar accent-bar--one"></div>
  <div class="accent-bar accent-bar--two"></div>
  <div class="accent-bar accent-bar--three"></div>
  <h1 class="brand-name">Meadowlark Health</h1>
  <div class="base-strip"></div>

  <div class="holder">
    <p class="holder__name">Danielle Ostrander</p>
    <p class="holder__role">RN, MSN, MHA Nurse Educator</p>
  </div>

  <ul class="contact">
    <li class="contact__item contact__item--phone">555.214.3096
      <svg class="contact__icon" viewBox="0 0 12 14" aria-label="cell"><rect x="2.5" y="0.8" width="7" height="12.4" rx="1" fill="none" stroke="#fff" stroke-width="1.2"/></svg>
    </li>
    <li class="contact__item contact__item--phone">555.470.2283
      <svg class="contact__icon" viewBox="0 0 12 14" aria-label="fax"><rect x="3" y="1" width="6" height="5" fill="none" stroke="#fff" stroke-width="1"/><rect x="1" y="6" width="10" height="6" fill="none" stroke="#fff" stroke-width="1"/><line x1="3" y1="9" x2="9" y2="9" stroke="#fff" stroke-width="1"/></svg>
    </li>
    <li class="contact__item contact__item--email">danielle.ostranderhealth@mailhub.com
      <svg class="contact__icon" viewBox="0 0 12 14" aria-label="email"><rect x="0.7" y="3.5" width="10.6" height="7.5" fill="none" stroke="#fff" stroke-width="1"/><polyline points="0.7,3.5 6,8 11.3,3.5" fill="none" stroke="#fff" stroke-width="1"/></svg>
    </li>
  </ul>
</section>

<section class="card card--back" aria-label="Business card back">
  <h2 class="brand-name">Meadowlark Health</h2>
</section>

</body>
</html>
```